Locksmith Store 475475 Signage

Design Brief: Locksmith Store Signage – "Locksmith 475475" [ΚΛΕΙΔΑΡΑΣ 475475 (in Greek)]
We are looking for a spectacular and professional sign design for the exterior of our locksmith store.
Signage Dimensions:
• Width: 6 meters
• Height: 1.5 meters
• Shopfront window Width: 6 meters, Height: 2.5 meters
Key Requirements (in order of importance):
1. It must be immediately clear that this is a locksmith store. [ΚΛΕΙΔΑΡΑΣ (in Greek)]
2. The store name "475475", (which is also the phone number 2310475475), should be highly visible and visually striking because this is the number that customers are calling when they are locked out.
3. The signage should also clearly communicate that except for house keys, which is obvious for a locksmith store the services we provide are:
o All kinds of house keys. ΚΛΕΙΔΙΑ ΣΠΙΤΙΩΝ(in Greek) (There is no key that we cannot do)
o Immobiliser car keys = ΚΛΕΙΔΙΑ ΑΥΤΟΚΙΝΗΤΩΝ (in Greek)
We unlock every car that exist, we program new immobilizer keys – remote controls, even if all keys are lost, we repair or change broken cells of car keys, we change batteries.
o High-security locks = ΚΛΕΙΔΑΡΙΕΣ ΑΣΦΑΛΕΙΑΣ (in Greek) we sell the best high security locks in the planet
o Armoured doors = ΠΟΡΤΕΣ ΑΣΦΑΛΕΙΑΣ (in Greek) (this may not be so important to be on the signage.
Visual Style:
We are open to creative direction, but the design should be eye-catching, professional, and modern, something that will stand out on a busy street and instantly tell customers who we are and what we offer. Also, you may use the shopfront window for graphic designs. Also, we are open if a part of the signage is digital.
________________________________________
Hello Designers,
Thank you so much for your effort and the designs you've shared.
I realized I forgot to mention that you can refer to my website at www.475475-keys.gr for more context.
Additionally, I’ve just uploaded two new photos: one showing the store with a black outline at the dimensions of the signage, and another with the large double-bit key placed in a different position to demonstrate that it is moveable.
Thanks again for your dedication!
every person that has a key

```html
<!DOCTYPE html>
<html lang="el">
<head>
<meta charset="utf-8">
<title>ΚΛΕΙΔΑΡΑΣ 475475 – Signage</title>
<link rel="stylesheet" href="https://fonts.googleapis.com/css2?family=Exo+2:wght@600&family=Orbitron:wght@900&family=Montserrat:wght@800&family=Open+Sans:wght@800&display=swap">
<style>
  :root {
    --backdrop: #bcbcbc;
    --black: #050505;
    --charcoal: #1d1d1d;
    --gold-light: #ffe680;
    --gold: #f2c33a;
    --gold-deep: #b8801a;
    --silver-light: #ffffff;
    --silver: #a9a9a9;
    --silver-dark: #5e5e5e;
    --white: #ffffff;
  }
  * { margin: 0; padding: 0; box-sizing: border-box; }
  html, body {
    width: 1200px; height: 1200px; overflow: hidden;
    background: var(--backdrop);
  }
  .sign {
    position: absolute; left: 27px; top: 458px;
    width: 1143px; height: 285px; overflow: hidden;
    background: radial-gradient(ellipse 60% 90% at 35% 35%, var(--charcoal) 0%, #0d0d0d 55%, var(--black) 100%);
    box-shadow: 6px 8px 14px rgba(0,0,0,0.35);
  }
  .sign-bands { position: absolute; inset: 0; }
  .key-art {
    position: absolute;
    border-radius: 40% 40% 8px 8px;
    opacity: 0.85;
  }
  .key-art.gold { background: radial-gradient(ellipse at 50% 70%, var(--gold) 0%, rgba(184,128,26,0.5) 55%, transparent 80%); }
  .key-art.silver { background: radial-gradient(ellipse at 50% 70%, var(--silver) 0%, rgba(94,94,94,0.45) 55%, transparent 80%); }
  .shop-title {
    position: absolute; left: 206px; top: 78px;
    font-family: "Exo 2", sans-serif; font-weight: 600;
    font-size: 68px; line-height: 1; letter-spacing: 1px;
    background: linear-gradient(180deg, var(--silver-light) 0%, #d6d6d6 45%, var(--silver-dark) 60%, #cfcfcf 100%);
    -webkit-background-clip: text; background-clip: text; color: transparent;
    filter: drop-shadow(0 0 6px rgba(255,255,255,0.35));
  }
  .shop-number {
    position: absolute; left: 156px; top: 150px;
    font-family: "Orbitron", sans-serif; font-weight: 900;
    font-size: 70px; line-height: 1; letter-spacing: 2px;
    background: linear-gradient(180deg, var(--gold-light) 0%, var(--gold) 50%, var(--gold-deep) 58%, var(--gold) 100%);
    -webkit-background-clip: text; background-clip: text; color: transparent;
    filter: drop-shadow(0 0 10px rgba(242,195,58,0.55));
  }
  .contact-phone {
    position: absolute; left: 766px; top: 33px;
    display: flex; align-items: center; gap: 12px;
  }
  .phone-icon { width: 40px; height: 40px; }
  .phone-number {
    font-family: "Montserrat", sans-serif; font-weight: 800;
    font-size: 42px; line-height: 1; letter-spacing: 0.5px;
    background: linear-gradient(180deg, var(--white) 0%, #e2e2e2 50%, var(--silver) 100%);
    -webkit-background-clip: text; background-clip: text; color: transparent;
  }
  .service-list {
    position: absolute; left: 778px; top: 88px;
    list-style: none;
    font-family: "Open Sans", sans-serif; font-weight: 800;
    font-size: 25px; line-height: 32.5px; color: var(--white);
  }
  .service-list li { display: flex; align-items: center; gap: 9px; }
  .service-list li::before {
    content: ""; width: 0; height: 0;
    border-top: 7px solid transparent; border-bottom: 7px solid transparent;
    border-left: 7px solid var(--gold);
  }
</style>
</head>
<body>
  <section class="sign">
    <svg class="sign-bands" width="1143" height="285" viewBox="0 0 1143 285">
      <defs>
        <linearGradient id="goldBand" x1="0" y1="0" x2="1" y2="0">
          <stop offset="0" stop-color="#f2c33a"/>
          <stop offset="0.45" stop-color="#ffe680"/>
          <stop offset="0.7" stop-color="#c98a1c"/>
          <stop offset="1" stop-color="#f5d36a"/>
        </linearGradient>
        <filter id="glow" x="-10%" y="-50%" width="120%" height="200%">
          <feGaussianBlur stdDeviation="3" result="b"/>
          <feMerge><feMergeNode in="b"/><feMergeNode in="SourceGraphic"/></feMerge>
        </filter>
      </defs>
      <g class="band-top-left" filter="url(#glow)">
        <polygon points="0,89 124,89 178,27 366,27 400,0 414,0 375,38 186,38 132,100 0,100" fill="url(#goldBand)"/>
        <rect x="0" y="115" width="150" height="2" fill="#f2c33a" opacity="0.8"/>
        <rect x="180" y="54" width="200" height="2" fill="#f2c33a" opacity="0.5"/>
      </g>
      <g class="band-bottom-right" filter="url(#glow)">
        <polygon points="740,285 796,232 1143,232 1143,247 806,247 760,285" fill="url(#goldBand)"/>
        <rect x="830" y="256" width="313" height="2" fill="#f2c33a" opacity="0.7"/>
      </g>
    </svg>

    <div class="key-art gold" role="img" aria-label="Gold double-bit key" style="left:32px; top:194px; width:84px; height:91px;"></div>
    <div class="key-art silver" role="img" aria-label="Silver antique key" style="left:93px; top:189px; width:87px; height:96px;"></div>
    <div class="key-art silver" role="img" aria-label="Silver antique key" style="left:593px; top:200px; width:68px; height:85px;"></div>
    <div class="key-art gold" role="img" aria-label="Gold house key" style="left:660px; top:204px; width:70px; height:81px;"></div>

    <h1 class="shop-title">ΚΛΕΙΔΑΡΑΣ</h1>
    <div class="shop-number">475.475</div>

    <div class="contact-phone">
      <svg class="phone-icon" viewBox="0 0 40 40" aria-hidden="true">
        <defs>
          <linearGradient id="goldDisc" x1="0" y1="0" x2="0" y2="1">
            <stop offset="0" stop-color="#ffe680"/>
            <stop offset="1" stop-color="#b8801a"/>
          </linearGradient>
        </defs>
        <circle cx="20" cy="20" r="19" fill="url(#goldDisc)"/>
        <path d="M13.5 10.5c1-.9 2-.7 2.6.2l2 3c.5.8.3 1.7-.4 2.3l-1.3 1c.9 2.2 2.6 4 4.7 5l1-1.3c.6-.7 1.6-.9 2.4-.3l3 2c.9.6 1 1.7.2 2.6l-1.5 1.7c-1 1-2.7 1.3-4.3.6-4.8-2-8.5-5.8-10.4-10.6-.6-1.6-.3-3.3.7-4.3z" fill="#111"/>
      </svg>
      <span class="phone-number">2310475475</span>
    </div>

    <ul class="service-list">
      <li>ΚΛΕΙΔΙΑ ΣΠΙΤΙΩΝ</li>
      <li>ΚΛΕΙΔΙΑ ΑΥΤΟΚΙΝΗΤΩΝ</li>
      <li>ΚΛΕΙΔΑΡΙΕΣ ΑΣΦΑΛΕΙΑΣ</li>
      <li>ΠΟΡΤΕΣ ΑΣΦΑΛΕΙΑΣ</li>
    </ul>
  </section>
</body>
</html>
```